Business Card Design Project - bel soravin group

dear Sirs

we need business card design for our group ( BEL Soravin Group ) , i have got the Logo design of our group from pixel harbor in previous , so all need details relating to our group i think available with you, as well as the the chosen logo design

we hope to provide us with business card logo that to be appropaite and satisfactory to us .

thanks

note : logo design of our group is attached .
Updates

Reason: please extend the deadline of my project for additional 15 days because i didn't received appropriate design for our gruop yet . kindly beaware that i have received 77 design till now , supossed to send me 200-250 design at least . thanks

Target Market(s)

contents
-

name : Korvan EL Mistrani

position : Operation Manager

Industry/Entity Type

Business

Requirements
Must have

• person name

group logo
Nice to have
• logo color matching with back background

```html
<!DOCTYPE html>
<html lang="en">
<head>
<meta charset="utf-8">
<title>BEL Soravin Group – Business Card</title>
<link rel="stylesheet" href="https://fonts.googleapis.com/css2?family=Open+Sans:wght@400;600;700&display=swap">
<style>
  :root {
    --bg: #e9e9ec;
    --blue-deep: #0f5d99;
    --blue-mid: #1f7fc0;
    --blue-light: #3a9bd6;
    --card-white: #f7f7f5;
    --grey-stripe: #8d8f93;
    --ink: #3c3d40;
    --white: #ffffff;
  }
  * { margin: 0; padding: 0; box-sizing: border-box; }
  html, body { width: 1200px; height: 900px; overflow: hidden; }
  body {
    background: var(--bg);
    font-family: "Open Sans", Arial, sans-serif;
    position: relative;
  }
  .card {
    position: absolute;
    left: 280px;
    width: 640px;
    height: 365px;
    border-radius: 22px;
    overflow: hidden;
    box-shadow: 0 8px 22px rgba(0,0,0,0.18);
  }
  .card-back { top: 60px; background: radial-gradient(ellipse at 45% 45%, var(--blue-light) 0%, var(--blue-mid) 45%, var(--blue-deep) 100%); }
  .card-front { top: 470px; background: var(--card-white); }
  .card-art { position: absolute; inset: 0; width: 100%; height: 100%; }

  .logo { position: absolute; display: flex; flex-direction: column; }
  .logo-row { display: flex; align-items: center; gap: 12px; }
  .logo-mark { width: 26px; height: 26px; }
  .logo-name { font-weight: 600; font-size: 50px; line-height: 1; letter-spacing: 1px; }
  .logo-tag { font-weight: 600; font-size: 19px; letter-spacing: 0.5px; margin-left: 40px; margin-top: 4px; }

  .card-back .logo { left: 150px; top: 120px; color: var(--white); }
  .card-back .logo-mark { background: var(--white); }
  .card-back .website { position: absolute; right: 34px; bottom: 30px; color: var(--white); font-size: 15px; font-weight: 600; }

  .card-front .logo { left: 58px; top: 120px; color: var(--blue-mid); }
  .card-front .logo-mark { background: var(--blue-mid); }
  .card-front .website { position: absolute; left: 160px; top: 20px; color: var(--blue-mid); font-size: 14px; font-weight: 600; }

  .person { position: absolute; right: 30px; top: 26px; text-align: right; color: var(--white); }
  .person-name { font-size: 24px; font-weight: 400; }
  .person-title { font-size: 11px; font-weight: 600; letter-spacing: 0.8px; text-transform: uppercase; margin-top: 2px; }

  .address { position: absolute; left: 150px; top: 262px; color: var(--ink); font-size: 15px; line-height: 1.3; }
  .divider { position: absolute; left: 345px; top: 265px; width: 1px; height: 70px; background: var(--ink); }
  .contacts { position: absolute; left: 362px; top: 258px; list-style: none; color: var(--ink); font-size: 15px; line-height: 1.16; }
  .contacts li { display: flex; align-items: center; gap: 10px; }
  .contacts svg { width: 14px; height: 14px; fill: var(--blue-mid); }
</style>
</head>
<body>

<section class="card card-back" aria-label="Card back">
  <svg class="card-art" viewBox="0 0 640 365" aria-hidden="true">
    <path d="M120,40 C300,10 480,30 640,90 L640,110 C480,60 300,45 120,70 Z" fill="rgba(255,255,255,0.10)"/>
    <path d="M160,110 C330,70 500,90 640,150 L640,175 C500,120 330,105 160,135 Z" fill="rgba(255,255,255,0.08)"/>
    <path d="M200,190 C360,150 520,170 640,220 L640,240 C520,195 360,185 200,210 Z" fill="rgba(255,255,255,0.06)"/>
  </svg>
  <div class="logo">
    <div class="logo-row"><span class="logo-mark"></span><span class="logo-name">BEL SORAVIN</span></div>
    <span class="logo-tag">GROUP OF COMPANIES</span>
  </div>
  <p class="website">www.belsoravin.com</p>
</section>

<section class="card card-front" aria-label="Card front">
  <svg class="card-art" viewBox="0 0 640 365" aria-hidden="true">
    <path d="M60,14 C230,-4 380,40 500,110 C560,145 610,165 640,170" fill="none" stroke="var(--grey-stripe)" stroke-width="10"/>
    <path d="M150,0 C300,10 420,55 520,112 C575,143 615,155 640,158 L640,0 Z" fill="var(--blue-mid)"/>
  </svg>
  <p class="website">www.belsoravin.com</p>
  <div class="person">
    <p class="person-name">Korvan EL Mistrani</p>
    <p class="person-title">Operation Manager</p>
  </div>
  <div class="logo">
    <div class="logo-row"><span class="logo-mark"></span><span class="logo-name">BEL SORAVIN</span></div>
    <span class="logo-tag">GROUP OF COMPANIES</span>
  </div>
  <address class="address" style="font-style:normal">
    P.O. Box: 48210<br>Dubai<br>United Arab Emirates
  </address>
  <span class="divider"></span>
  <ul class="contacts">
    <li><svg viewBox="0 0 16 16"><path d="M2 6c0-2 2-3 6-3s6 1 6 3l-2 1-1-2H5L4 7 2 6zM4 8h8l1 5H3z"/></svg>+123 456 7890</li>
    <li><svg viewBox="0 0 16 16"><path d="M5 1h6v14H5zM6 3v8h4V3z"/></svg>+123 456 7890</li>
    <li><svg viewBox="0 0 16 16"><path d="M4 1h7v4H4zM2 6h12v8H2zM4 8v2h8V8z"/></svg>+123 456 7890</li>
    <li><svg viewBox="0 0 16 16"><path d="M1 4h14v9H1zM2 5l6 4 6-4v-0z" /></svg>info@belsoravin.com</li>
  </ul>
</section>

</body>
</html>
```